Sorlen cards

I want a simple business card that pops.
Logo on one side.
On side two i want.
"Are you thinking about a new building on your property, or renovating an existing structure? Contact".....
Owners Name: Dale Whitcombe
Owners Phone number: 555-555-0192
Address:4716 Oxtail Ridge RD, Larkfield, ST 00000
Committed to Quality, Service, and Integrity

```html
<!DOCTYPE html>
<html lang="en">
<head>
<meta charset="UTF-8">
<title>Sorlen Builders – Business Cards</title>
<link href="https://fonts.googleapis.com/css2?family=Anton&family=Poppins:wght@300;400;700&display=swap" rel="stylesheet">
<style>
  :root {
    --stage: #2a2a2a;
    --card-white: #ffffff;
    --brown-deep: #3d2a1b;
    --brown-mid: #6e4f36;
    --brown-light: #a88f74;
    --ink-light: #ffffff;
  }
  * { box-sizing: border-box; margin: 0; padding: 0; }
  html, body {
    width: 1200px; height: 689px; overflow: hidden;
    background: var(--stage);
  }
  .canvas { position: relative; width: 1200px; height: 689px; }
  .card {
    position: absolute; top: 190px;
    width: 540px; height: 309px;
    border-radius: 18px; overflow: hidden;
    box-shadow: 0 14px 30px rgba(0,0,0,.45);
  }
  .card--front { left: 40px; background: var(--card-white); }
  .card--back  { left: 620px; background: var(--brown-deep); }

  .wordmark {
    position: absolute; left: 46px; top: 118px;
    display: flex; align-items: center; gap: 14px;
    color: var(--brown-deep);
    font-family: "Poppins", sans-serif; font-weight: 700;
  }
  .wordmark__square { width: 44px; height: 44px; background: var(--brown-deep); }
  .wordmark__name { font-size: 44px; line-height: 1; letter-spacing: 1px; }
  .wordmark__sub  { font-size: 15px; letter-spacing: 3px; line-height: 1.3; }

  .decor {
    position: absolute;
    background: linear-gradient(135deg, var(--brown-light) 0%, var(--brown-mid) 55%, var(--brown-deep) 100%);
  }
  .card--front .decor { right: 0; top: 0; width: 215px; height: 100%; }
  .card--back  .decor { left: 0; top: 0; width: 230px; height: 100%;
    background: linear-gradient(160deg, var(--brown-mid) 0%, var(--brown-light) 50%, var(--brown-mid) 100%); opacity: .85; }

  .info {
    position: absolute; left: 252px; top: 26px; right: 24px;
    color: var(--ink-light);
  }
  .info__pitch {
    font-family: "Anton", sans-serif; font-size: 19px; line-height: 1.2;
    text-transform: uppercase; letter-spacing: .4px;
  }
  .info__rule { height: 1px; background: var(--ink-light); opacity: .8; margin: 12px 0 10px; }
  .info__label { font-family: "Poppins", sans-serif; font-weight: 300; font-size: 13px; }
  .info__name {
    font-family: "Poppins", sans-serif; font-weight: 400; font-size: 20px;
    letter-spacing: .5px; margin-top: 4px;
  }
  .info__row {
    display: flex; align-items: flex-start; gap: 8px;
    font-family: "Poppins", sans-serif; font-weight: 300; font-size: 13px; line-height: 1.35;
    margin-top: 6px;
  }
  .info__row svg { flex: 0 0 16px; margin-top: 1px; }
  .info__tagline {
    font-family: "Anton", sans-serif; font-size: 12.5px; letter-spacing: .3px;
    border-top: 1px solid rgba(255,255,255,.8); padding-top: 7px; margin-top: 12px;
  }
</style>
</head>
<body>
<main class="canvas">
  <section class="card card--front" aria-label="Front of card">
    <div class="wordmark">
      <span class="wordmark__square"></span>
      <div>
        <div class="wordmark__name">SORLEN</div>
        <div class="wordmark__sub">BUILDERS LLC</div>
      </div>
    </div>
    <div class="decor" role="img" aria-label="Large brand symbol decoration in brown tones"></div>
  </section>

  <section class="card card--back" aria-label="Back of card">
    <div class="decor" role="img" aria-label="Large brand symbol decoration in brown tones"></div>
    <div class="info">
      <p class="info__pitch">Are you thinking about a new building on your property, or renovating an existing structure?</p>
      <div class="info__rule"></div>
      <p class="info__label">Contact</p>
      <p class="info__name">DALE WHITCOMBE</p>
      <div class="info__row">
        <svg width="16" height="16" viewBox="0 0 16 16" aria-hidden="true">
          <circle cx="8" cy="8" r="8" fill="#fff"/>
          <path d="M5.2 4.3l1.3-.3.8 1.9-.9.7a5 5 0 0 0 2.3 2.3l.7-.9 1.9.8-.3 1.3c-3.2.3-6.1-2.6-5.8-5.8z" fill="#3d2a1b"/>
        </svg>
        <span>555-555-0192</span>
      </div>
      <div class="info__row">
        <svg width="16" height="16" viewBox="0 0 16 16" aria-hidden="true">
          <circle cx="8" cy="8" r="8" fill="#fff"/>
          <path d="M8 3.5a3 3 0 0 0-3 3c0 2.2 3 5.5 3 5.5s3-3.3 3-5.5a3 3 0 0 0-3-3zm0 4.2a1.2 1.2 0 1 1 0-2.4 1.2 1.2 0 0 1 0 2.4z" fill="#3d2a1b"/>
        </svg>
        <span>4716 Oxtail Ridge RD,<br>Larkfield, ST 00000</span>
      </div>
      <p class="info__tagline">Committed to Quality, Service and Integrity</p>
    </div>
  </section>
</main>
</body>
</html>
```